Gobo Flyer to generate sales and to use at trade shows or as a leave behind to client

We are looking to create a flyer to promote our new exterior or interior event lighting options. We are looking for the layout to be clean and consistent with our color scheme. We are a professional technologically advanced company looking to take your event to the next level. We are looking for a layout which has an image at the top as well as a few other images to allow reader to see a few options

Target Market(s)

Residential as well as commercial

Industry/Entity Type

Trade

Requirements
Must have
• Need the round images to create a collage. and include the text samples of what is available

```html
<!DOCTYPE html>
<html lang="en">
<head>
<meta charset="utf-8">
<title>Projected Illuminations Flyer</title>
<link href="https://fonts.googleapis.com/css2?family=Exo+2:wght@600;700;800&family=Lato:ital,wght@0,400;0,700;1,700;1,900&family=Roboto+Condensed:wght@400;500&display=swap" rel="stylesheet">
<style>
  :root {
    --blue: #1a86e0;
    --blue-deep: #0d3f9e;
    --blue-mid: #1565c8;
    --charcoal: #393939;
    --panel-light: #efefef;
    --ink: #222;
    --pink: #f0145c;
    --white: #fff;
  }
  * { margin: 0; padding: 0; box-sizing: border-box; }
  html, body { width: 902px; height: 1200px; overflow: hidden; background: #fff; }
  .flyer { position: relative; width: 902px; height: 1200px; overflow: hidden; font-family: "Lato", sans-serif; }
  .hero-photo {
    position: absolute; left: 0; top: 0; width: 902px; height: 420px;
    background: radial-gradient(ellipse at 38% 35%, #c0303c 0%, #6a1e3e 30%, #2a1434 60%, #120c1a 100%);
  }
  .hero-photo::after {
    content: ""; position: absolute; left: 0; right: 0; bottom: 0; height: 150px;
    background: linear-gradient(transparent, rgba(170,130,230,.75));
  }
  .shapes { position: absolute; left: 0; top: 0; }
  .brand {
    position: absolute; left: 585px; top: 62px;
    display: flex; align-items: center; gap: 12px;
    font-family: "Exo 2", sans-serif; font-weight: 700; font-size: 28px;
    line-height: 1.05; color: var(--blue-mid); letter-spacing: 1px;
  }
  .brand-mark { width: 26px; height: 26px; background: var(--blue-mid); flex: none; }
  .headline {
    position: absolute; left: 0; width: 902px; top: 436px; text-align: center;
    font-family: "Exo 2", sans-serif; font-weight: 800; font-size: 58px;
    color: var(--white); letter-spacing: 1px; line-height: 70px;
  }
  .option {
    position: absolute; width: 240px; height: 240px; border-radius: 50%;
    border: 8px solid var(--white); box-shadow: 0 0 0 9px var(--blue-deep), 0 4px 12px 9px rgba(0,0,0,.3);
  }
  .option-white { left: 45px; top: 524px; background: radial-gradient(circle at 50% 40%, #e8e0f0 0%, #7c6f8a 35%, #2b2a3a 60%, #6a4a2a 80%, #3a2a1a 100%); }
  .option-violet { left: 331px; top: 524px; background: radial-gradient(circle at 50% 40%, #d050d0 0%, #5a3ad0 35%, #2a2050 60%, #6a4a2a 80%, #3a2a1a 100%); }
  .option-green { left: 625px; top: 524px; background: radial-gradient(circle at 50% 40%, #50e0a0 0%, #2a8a6a 30%, #d04040 45%, #2a2a3a 62%, #6a4a2a 80%, #3a2a1a 100%); }
  .tab {
    position: absolute; height: 46px; background: var(--blue); color: var(--white);
    font-weight: 700; font-size: 22px; line-height: 46px; border-radius: 0 12px 12px 0;
  }
  .tab-events { left: 0; top: 806px; width: 398px; padding-left: 32px; }
  .tab-offer { left: 530px; top: 806px; width: 372px; padding-left: 14px; border-radius: 12px 0 0 12px; }
  .occasions { position: absolute; left: 30px; top: 870px; list-style: none; }
  .occasions li {
    position: relative; padding-left: 38px; height: 33.6px; line-height: 33.6px;
    color: var(--white); font-style: italic; font-weight: 700; font-size: 21px;
  }
  .occasions li::before {
    content: ""; position: absolute; left: 0; top: 11px; width: 12px; height: 12px;
    border-radius: 50%; background: var(--blue);
  }
  .offer-copy {
    position: absolute; left: 508px; top: 868px; width: 372px;
    font-size: 13px; line-height: 17px; color: var(--ink); text-align: justify;
  }
  .offer-price { position: absolute; right: 26px; top: 936px; text-align: right; }
  .rent { font-family: "Roboto Condensed", sans-serif; font-weight: 500; font-size: 34px; color: var(--blue-mid); line-height: 40px; }
  .low { font-family: "Roboto Condensed", sans-serif; font-size: 24px; color: var(--ink); line-height: 50px; }
  .amount { font-size: 50px; font-weight: 500; color: var(--pink); vertical-align: -4px; }
  .nights { font-style: italic; font-weight: 900; font-size: 23px; color: var(--ink); line-height: 26px; }
  .includes {
    position: absolute; left: 512px; top: 1080px; display: flex; gap: 8px;
    font-family: "Roboto Condensed", sans-serif; font-size: 13.5px; color: var(--ink); list-style: none;
  }
  .includes li::before { content: "\25CF"; color: var(--blue-mid); margin-right: 5px; font-size: 11px; }
  .website {
    position: absolute; left: 0; width: 902px; top: 1145px; text-align: center;
    color: var(--white); font-weight: 700; font-size: 18px;
  }
</style>
</head>
<body>
<div class="flyer">
  <div class="hero-photo" role="img" aria-label="Two-storey house at night with red heart shapes projected on the facade and a violet-lit front porch"></div>

  <svg class="shapes" width="902" height="1200" viewBox="0 0 902 1200" aria-hidden="true">
    <rect x="0" y="560" width="458" height="600" fill="var(--charcoal)"/>
    <rect x="458" y="560" width="444" height="600" fill="var(--panel-light)"/>
    <path d="M0,343 Q451,450 902,337 L902,600 Q560,640 458,700 L0,700 Z" fill="var(--blue)"/>
    <path d="M0,650 Q300,560 902,610 L902,560 Q500,520 0,600 Z" fill="#1573cc" opacity=".6"/>
    <path d="M0,700 L0,650 Q300,560 902,610 L902,640 L458,640 L458,700 Z" fill="var(--charcoal)"/>
    <path d="M458,640 L902,640 L902,610 Q680,590 458,640 Z" fill="var(--panel-light)"/>
    <path d="M0,343 Q451,450 902,337" fill="none" stroke="var(--white)" stroke-width="7"/>
    <path d="M500,0 L902,0 L902,182 Q760,210 640,190 Q540,160 500,0 Z" fill="var(--blue-mid)"/>
    <path d="M500,0 L902,0 L902,168 Q760,192 650,176 Q548,150 500,0 Z" fill="var(--white)"/>
    <path d="M0,1150 Q450,1080 902,1120 L902,1200 L0,1200 Z" fill="var(--blue-deep)"/>
    <path d="M0,1160 Q450,1094 902,1132 L902,1200 L0,1200 Z" fill="var(--blue)"/>
  </svg>

  <div class="brand"><span class="brand-mark"></span><span>QUELLARO<br>LIGHTS</span></div>

  <h1 class="headline">PROJECTED ILLUMINATIONS</h1>

  <div class="option option-white" role="img" aria-label="Brick house at dusk lit with white wall washers"></div>
  <div class="option option-violet" role="img" aria-label="Brick house at dusk lit in violet, blue and red"></div>
  <div class="option option-green" role="img" aria-label="Brick house at dusk lit in green and red"></div>

  <div class="tab tab-events">Perfect for Special Events</div>
  <ul class="occasions">
    <li>Parties</li>
    <li>Graduation</li>
    <li>Holidays</li>
    <li>Weddings</li>
    <li>Business Promotions</li>
    <li>Anytime you want to celebrate</li>
  </ul>

  <div class="tab tab-offer">Illuminate a projected light</div>
  <p class="offer-copy">Illuminate a projected light design and 2 colored wall washers on the exterior or interior of your home business or special event. Choose from many stock designs or customize the image to make the design truly your own.</p>

  <div class="offer-price">
    <div class="rent">Rent it today</div>
    <div class="low">FOR AS LOW AS <span class="amount">$399</span></div>
    <div class="nights">for a one night rental</div>
  </div>

  <ul class="includes">
    <li>Including Illuminator</li>
    <li>2 wall washer</li>
    <li>Installation and Removal</li>
  </ul>

  <div class="website">www.quellaro-lights.example</div>
</div>
</body>
</html>
```